Official personalized stationery with official coat of arms

I am looking for custom stationery design such as US letter size (8.5 X 11 or 21.6cm X 27.9cm), email signature (email) and envelope for US letter size (standard envelope no. 10 or 10.5cm X 24.5cm). Inspired by my personal coat of arms and my postal address:

4186 rue des Saules
Levis, Quebec, G7K 3M2
Canada

Ideally a discreet design based on the coat of arms of Lucien Morvand but inspired by my mother's original coat of arms.

Something golden and translucent, simple but tasteful, without overemphasizing the green color. The coat of arms should have green, but not the entire structure of the stationery.

I am also looking for a small official thank you card in half letter size.

The design must be with the Lucien Morvand coat of arms and not the full coat of arms

Target Market(s)

For official communication

Industry/Entity Type

Communication officiel et parlementaire

Font styles to use
Other font styles liked:
• J’aime bien l’écriture comme le logo de la maison Velloze la police pour écrire le nom Velloze

Requirements
Must have
• Simplicity and use the Lucien Morvand coat of arms and not the full coat of arms
Nice to have
• Official and royal appearance as it is an official heraldic title of the British crown
Should not have
• Email and website

```html
<!DOCTYPE html>
<html lang="fr">
<head>
<meta charset="utf-8">
<title>Henri Duchesne — Papeterie officielle</title>
<link rel="stylesheet" href="https://fonts.googleapis.com/css2?family=Libre+Caslon+Text:wght@400;700&family=Cormorant+Garamond:ital,wght@1,500&family=Open+Sans:wght@400&display=swap">
<style>
  :root {
    --stage-light: #d9d9d9;
    --stage-dark: #b3b3b3;
    --paper: #ffffff;
    --paper-shade: #f1f1f1;
    --heraldic-green: #2b6b35;
    --gold: #b98a2e;
    --label-green: #2f5f35;
  }
  * { box-sizing: border-box; margin: 0; padding: 0; }
  html, body { width: 1200px; height: 548px; overflow: hidden; }
  body { position: relative; background: var(--stage-light); font-family: "Libre Caslon Text", Georgia, serif; }

  .stage-right { position: absolute; left: 685px; top: 0; width: 515px; height: 548px; background: var(--stage-dark); }

  .sheet { position: absolute; background: var(--paper); box-shadow: 0 3px 10px rgba(0,0,0,.18); }

  .crest-name {
    display: inline-flex; align-items: center; gap: 4px;
    color: var(--heraldic-green); font-weight: 700; letter-spacing: .12em; white-space: nowrap;
  }
  .crest-name .crest-square { width: 7px; height: 7px; border: 1px solid var(--heraldic-green); }

  .signature-name { font-family: "Cormorant Garamond", Georgia, serif; font-style: italic; font-weight: 500; color: var(--gold); line-height: 1; white-space: nowrap; }
  .address { color: var(--heraldic-green); text-transform: uppercase; letter-spacing: .06em; white-space: nowrap; }
  .address span + span { margin-left: 1.4em; }

  .piece-label {
    position: absolute; font-family: "Open Sans", Arial, sans-serif; font-size: 7px;
    color: var(--label-green); text-transform: uppercase; letter-spacing: .03em; white-space: nowrap;
  }

  /* Letterhead */
  .letterhead { left: 40px; top: 40px; width: 250px; height: 324px; }
  .letterhead .head { position: absolute; top: 30px; width: 100%; text-align: center; }
  .letterhead .crest-name { font-size: 7px; }
  .letterhead .office { margin-top: 8px; font-size: 4px; color: var(--heraldic-green); font-weight: 700; letter-spacing: .1em; }
  .letterhead .signature-name { font-size: 12px; margin-top: 3px; }
  .letterhead .foot { position: absolute; bottom: 22px; width: 100%; display: flex; justify-content: center; align-items: center; gap: 10px; font-size: 4px; }
  .letterhead .foot span + span { margin-left: 0; }
  .ornament { width: 5px; height: 5px; border-radius: 50%; background: var(--gold); }

  /* Name cards */
  .card { width: 150px; height: 86px; }
  .card-front { left: 360px; top: 40px; }
  .card-back { left: 520px; top: 40px; display: flex; align-items: center; justify-content: center; }
  .card-front .signature-name { position: absolute; top: 26px; width: 100%; text-align: center; font-size: 13px; }
  .card-front .address { position: absolute; bottom: 14px; width: 100%; text-align: center; font-size: 3.4px; }
  .card-back .crest-name { font-size: 8px; }

  /* Envelope */
  .envelope { left: 360px; top: 190px; width: 310px; height: 135px; background: linear-gradient(#f6f6f6, var(--paper-shade)); }
  .envelope .crest-name { position: absolute; top: 18px; left: 0; width: 100%; justify-content: center; font-size: 7px; }
  .envelope .sender { position: absolute; left: 20px; bottom: 18px; }
  .envelope .signature-name { font-size: 11px; margin-bottom: 3px; }
  .envelope .address { font-size: 3.6px; }

  /* Email header */
  .email-header { left: 769px; top: 230px; width: 347px; height: 88px; display: flex; align-items: center; padding-left: 40px; gap: 12px; }
  .email-header .crest-name { font-size: 6px; }
  .email-header .signature-name { font-size: 11px; }
  .email-header .address { font-size: 3.6px; }
</style>
</head>
<body>
  <div class="stage-right"></div>

  <article class="sheet letterhead">
    <header class="head">
      <div class="crest-name"><span class="crest-square"></span>DUCHESNE</div>
      <p class="office">DU BUREAU DE</p>
      <p class="signature-name">Henri Duchesne</p>
    </header>
    <footer class="foot address">
      <span>4186 rue des Saules</span>
      <span class="ornament" role="img" aria-label="Petit ornement floral doré"></span>
      <span>Levis, Quebec, G7K 3M2</span>
      <span>Canada</span>
    </footer>
  </article>
  <p class="piece-label" style="left:130px; top:380px;">Letter head</p>

  <section class="sheet card card-front">
    <p class="signature-name">Henri Duchesne</p>
    <p class="address"><span>4186 rue des Saules</span><span>Levis, Quebec, G7K 3M2</span><span>Canada</span></p>
  </section>
  <section class="sheet card card-back">
    <div class="crest-name"><span class="crest-square"></span>DUCHESNE</div>
  </section>
  <p class="piece-label" style="left:490px; top:140px;">Name card</p>

  <section class="sheet envelope">
    <div class="crest-name"><span class="crest-square"></span>DUCHESNE</div>
    <div class="sender">
      <p class="signature-name">Henri Duchesne</p>
      <p class="address"><span>4186 rue des Saules</span><span>Levis, Quebec, G7K 3M2</span><span>Canada</span></p>
    </div>
  </section>
  <p class="piece-label" style="left:490px; top:340px;">Envelope</p>

  <section class="sheet email-header">
    <div class="crest-name"><span class="crest-square"></span>DUCHESNE</div>
    <p class="signature-name">Henri Duchesne</p>
    <p class="address"><span>4186 rue des Saules</span><span>Levis, Quebec, G7K 3M2</span><span>Canada</span></p>
  </section>
  <p class="piece-label" style="left:918px; top:354px;">Email header</p>
</body>
</html>
```